Award winning pet photographer needs business card and letterhead

Business card and letterhead for our Pet photography business. We specialize in studio portraits of dogs.

Target Market(s)

Wealthy and middle class dog owners who would like photos of their dogs as wall art.

Industry/Entity Type

Portrait Photography

Contact Information for Business Card

Our business name is Tails of Glee Pet Photography. Would be good to include dog and a heart, bright colours and a modern design

Font styles to use
Sans Serif

Colors
f04a50
f68d4d
faa54b
33a6d7
33b8a4
abd036

Requirements
Must have
• Business name: Tails of Glee Pet Photography
• Phone number: 0497 560314
• Email: marcus@kwstudio.com.au
• Website:www.tailsofglee.com.au
• Photographer: Marcus Holloway
Nice to have
• In Addition letterhead should include
• Studio address 27 Fennick Court, Leederville 6007
• Postal Address 8 Ormsby Ave, West Leederville 6007

```html
<!DOCTYPE html>
<html lang="en">
<head>
<meta charset="utf-8">
<title>Tails of Glee Pet Photography – Business Cards</title>
<link rel="stylesheet" href="https://fonts.googleapis.com/css2?family=Questrial&display=swap">
<style>
  :root {
    --canvas: #eceae6;
    --card: #ffffff;
    --coral: #f04a50;
    --teal: #33b8a4;
    --mint: #7fd9c6;
    --ghost: #efefef;
    --white: #ffffff;
  }
  html, body {
    margin: 0;
    padding: 0;
    width: 1200px;
    height: 784px;
    overflow: hidden;
    background: var(--canvas);
    font-family: "Questrial", "Century Gothic", sans-serif;
  }
  .canvas {
    position: relative;
    width: 1200px;
    height: 784px;
  }
  .card {
    position: absolute;
    width: 540px;
    height: 330px;
    background: var(--card);
    overflow: hidden;
    box-shadow: 0 2px 6px rgba(0,0,0,0.12);
  }
  .card--back { left: 70px; top: 70px; }
  .card--front { left: 590px; top: 384px; }

  .brand {
    position: absolute;
    display: flex;
    align-items: center;
    gap: 14px;
    color: var(--teal);
    z-index: 1;
  }
  .brand__dot {
    width: 46px;
    height: 46px;
    border-radius: 50%;
    background: var(--coral);
    flex: none;
  }
  .brand__name {
    font-size: 28px;
    line-height: 1.05;
    letter-spacing: 1px;
    text-transform: uppercase;
  }
  .brand__name small {
    display: block;
    font-size: 16px;
    letter-spacing: 3px;
  }
  .card--back .brand { left: 70px; top: 118px; }
  .card--front .brand { left: 40px; top: 78px; }

  .ghost-name {
    position: absolute;
    right: 28px;
    top: 190px;
    font-size: 50px;
    line-height: 0.95;
    color: var(--ghost);
    text-transform: uppercase;
    text-align: right;
  }

  .swoosh {
    position: absolute;
    inset: 0;
    width: 540px;
    height: 330px;
  }

  .contact {
    position: absolute;
    left: 352px;
    top: 186px;
    color: var(--white);
  }
  .contact__name {
    font-size: 16px;
    color: var(--mint);
    margin: 0;
  }
  .contact__role {
    font-size: 9px;
    margin: 1px 0 12px;
  }
  .contact__list {
    list-style: none;
    margin: 0;
    padding: 0;
  }
  .contact__list li {
    display: flex;
    align-items: center;
    gap: 6px;
    font-size: 11.5px;
    height: 20px;
    white-space: nowrap;
  }
  .contact__icon {
    width: 13px;
    height: 13px;
    flex: none;
  }
</style>
</head>
<body>
<main class="canvas">

  <section class="card card--back" aria-label="Business card back">
    <div class="ghost-name" aria-hidden="true">Tails<br>of Glee</div>
    <div class="brand">
      <span class="brand__dot"></span>
      <div class="brand__name">Tails of Glee<small>Pet Photography</small></div>
    </div>
  </section>

  <section class="card card--front" aria-label="Business card front">
    <svg class="swoosh" viewBox="0 0 540 330" aria-hidden="true">
      <path d="M285,168 C390,135 480,75 540,8 L540,38 C470,110 380,155 285,168 Z" fill="var(--teal)"/>
      <path d="M110,330 C230,250 410,190 540,40 L540,330 Z" fill="var(--coral)"/>
    </svg>

    <div class="brand">
      <span class="brand__dot"></span>
      <div class="brand__name">Tails of Glee<small>Pet Photography</small></div>
    </div>

    <div class="contact">
      <p class="contact__name">Marcus Holloway</p>
      <p class="contact__role">Photographer</p>
      <ul class="contact__list">
        <li>
          <svg class="contact__icon" viewBox="0 0 14 14" aria-hidden="true">
            <circle cx="7" cy="7" r="6.3" fill="none" stroke="#fff" stroke-width="1"/>
            <path d="M5,3.8 L6.2,5.6 L5.6,6.3 C6,7.3 6.7,8 7.7,8.4 L8.4,7.8 L10.2,9 L9.5,10.2 C7,10 4,7 3.8,4.5 Z" fill="#fff"/>
          </svg>
          0497 560314
        </li>
        <li>
          <svg class="contact__icon" viewBox="0 0 14 14" aria-hidden="true">
            <circle cx="7" cy="7" r="6.3" fill="none" stroke="#fff" stroke-width="1"/>
            <rect x="3.8" y="4.8" width="6.4" height="4.4" fill="none" stroke="#fff" stroke-width="0.9"/>
            <path d="M3.8,4.8 L7,7.4 L10.2,4.8" fill="none" stroke="#fff" stroke-width="0.9"/>
          </svg>
          marcus@kwstudio.com.au
        </li>
        <li>
          <svg class="contact__icon" viewBox="0 0 14 14" aria-hidden="true">
            <circle cx="7" cy="7" r="6.3" fill="none" stroke="#fff" stroke-width="1"/>
            <circle cx="7" cy="7" r="3.4" fill="none" stroke="#fff" stroke-width="0.8"/>
            <path d="M3.6,7 H10.4 M7,3.6 C5.6,5.4 5.6,8.6 7,10.4 M7,3.6 C8.4,5.4 8.4,8.6 7,10.4" fill="none" stroke="#fff" stroke-width="0.7"/>
          </svg>
          www.tailsofglee.com.au
        </li>
      </ul>
    </div>
  </section>

</main>
</body>
</html>
```